2022 Landscaping Services

Please use the prior year design as an example. Similar style but DO NOT COPY IT EXACTLY- you can use different photos from our website if you like. Same text for year 2022.
Design should clearly depict the differences between the 3 products so people can buy one of them. Be creative!

size 8.5" x 11"

Must provide source file in photoshop if you are winner

• Same text as original flier but with year 2022

```html
<!DOCTYPE html>
<html lang="en">
<head>
<meta charset="utf-8">
<title>Elmwood Grove Cemetery – 2022 Gravesite Landscaping Package</title>
<link rel="stylesheet" href="https://fonts.googleapis.com/css2?family=Montserrat:wght@400;500;600;700&family=Kaushan+Script&display=swap">
<style>
:root{
  --maroon:#7a2230;
  --maroon-dark:#6a1c29;
  --stone:#dcd7d4;
  --ink:#1f2340;
  --white:#ffffff;
  --backdrop:#c1c5cc;
  --photo-a:#3d3a22;
  --photo-b:#9a8a3c;
  --photo-c:#e8c85a;
}
*{margin:0;padding:0;box-sizing:border-box}
html,body{width:1200px;height:1021px;overflow:hidden;background:var(--backdrop);font-family:"Montserrat",sans-serif;color:var(--ink)}
.flyer{position:absolute;left:266px;top:79px;width:668px;height:865px;background:var(--white);overflow:hidden}
.hero{position:absolute;left:0;top:0}
.brand{position:absolute;left:0;top:36px;width:219px;height:53px;background:var(--white);display:flex;align-items:center;justify-content:center;gap:8px}
.brand-dot{width:14px;height:14px;border:1.5px solid var(--maroon);border-radius:50%}
.brand-name{font-size:11px;font-weight:600;color:var(--maroon);letter-spacing:.06em}
.title{position:absolute;right:21px;top:250px;text-align:right;color:var(--white);font-weight:700;line-height:1}
.title .year{font-size:48px;display:block;margin-bottom:8px}
.title .line{font-size:33px;display:block;margin-bottom:8px;letter-spacing:.01em}
.services{position:absolute;left:19px;top:419px;width:150px}
.services h2{font-size:19.5px;font-weight:700;color:var(--maroon);line-height:1;letter-spacing:.01em}
.service-list{list-style:none;position:absolute;left:19px;top:0}
.service-item{position:absolute;left:0;width:150px;font-size:9.5px;font-weight:600;line-height:13px;letter-spacing:.03em;white-space:nowrap}
.valid{position:absolute;left:19px;top:735px;font-size:14.5px;font-weight:600;line-height:18px}
.plan{position:absolute;text-align:center}
.plan-head{position:absolute;left:0;right:0;display:flex;flex-direction:column;align-items:center;justify-content:center;line-height:1.1}
.plan-name{font-size:14px;font-weight:600;letter-spacing:.03em}
.plan-sub{font-size:10.5px;font-weight:500;letter-spacing:.05em}
.plan-freq{position:absolute;left:0;right:0;font-size:7.5px;line-height:10px;font-weight:500}
.plan-side{width:149px;top:411px;height:378px}
.plan-side .plan-head{top:0;height:48px;background:var(--stone);color:var(--ink)}
.plan-side .plan-body{position:absolute;top:48px;left:0;right:0;bottom:0;background:var(--maroon);color:var(--white)}
.seasonal{left:176px}
.basic{left:505px}
.perpetual{left:325px;top:396px;width:180px;height:413px;background:var(--white);box-shadow:0 2px 6px rgba(0,0,0,.25);z-index:2}
.perpetual .plan-head{top:0;height:63px;background:var(--maroon);color:var(--white)}
.perpetual .plan-name{font-size:15px}
.perpetual .plan-sub{font-size:11px}
.perpetual .plan-freq{color:var(--maroon)}
.badge{position:absolute;left:481px;top:386px;width:42px;height:42px;border-radius:50%;background:var(--white);box-shadow:0 1px 3px rgba(0,0,0,.3);z-index:3;display:flex;flex-direction:column;align-items:center;justify-content:center;font-family:"Kaushan Script",cursive;color:var(--maroon);font-size:9px;line-height:9px}
.mark{position:absolute;left:50%;width:16px;height:16px;margin-left:-8px}
.rule{position:absolute;height:1.5px;background:var(--white)}
.perpetual .rule{background:var(--maroon);height:2.5px}
.price-row{position:absolute;left:8px;right:8px;display:flex;justify-content:space-between}
.price{flex:1;display:flex;flex-direction:column;align-items:center;border-left:1px solid rgba(255,255,255,.8)}
.price:first-child{border-left:none}
.price b{font-size:14px;font-weight:600;line-height:15px}
.price small{font-size:5.5px}
.price-big{position:absolute;left:0;right:0;font-weight:600;line-height:1}
.note{position:absolute;left:0;right:0;font-size:7px;line-height:10px}
.footer-band{position:absolute;left:0;top:830px;width:273px;height:35px;background:var(--maroon);color:var(--white);font-size:11px;font-weight:600;display:flex;align-items:center;padding-left:23px;letter-spacing:.02em}
.footer-contact{position:absolute;left:273px;top:836px;width:395px;text-align:center;font-size:11.5px;font-weight:500;color:var(--maroon);letter-spacing:.02em}
.footer-rule{position:absolute;left:273px;top:852px;width:395px;height:3px;background:var(--maroon)}
</style>
</head>
<body>
<main class="flyer">
  <svg class="hero" width="668" height="412" viewBox="0 0 668 412" aria-hidden="false">
    <defs>
      <linearGradient id="autumn" x1="0" y1="0" x2="1" y2="1">
        <stop offset="0" stop-color="var(--photo-b)"/>
        <stop offset=".5" stop-color="var(--photo-a)"/>
        <stop offset="1" stop-color="var(--photo-b)"/>
      </linearGradient>
      <radialGradient id="sun" cx=".8" cy=".3" r=".5">
        <stop offset="0" stop-color="var(--photo-c)" stop-opacity=".9"/>
        <stop offset="1" stop-color="var(--photo-c)" stop-opacity="0"/>
      </radialGradient>
    </defs>
    <g role="img" aria-label="Photograph of a cemetery path lined with headstones under golden autumn trees at sunset">
      <rect width="668" height="330" fill="url(#autumn)"/>
      <rect width="668" height="330" fill="url(#sun)"/>
    </g>
    <polygon points="0,316 668,220 668,412 0,412" fill="var(--maroon)"/>
  </svg>

  <div class="brand"><span class="brand-dot"></span><span class="brand-name">ELMWOOD GROVE CEMETERY</span></div>

  <h1 class="title"><span class="year">2022</span><span class="line">GRAVESITE</span><span class="line">LANDSCAPING PACKAGE</span></h1>

  <section class="services">
    <h2>SERVICES<br>OFFERED</h2>
  </section>
  <ul class="service-list">
    <li class="service-item" style="top:470px">WEDDING &amp; TRIMMING ON<br>YOUR GRAVESITE</li>
    <li class="service-item" style="top:506px">PAYMENT ENSURED<br>FOREVER GRAVE CAR</li>
    <li class="service-item" style="top:542px">WEDDING &amp; TRIMMING ON<br>YOUR GRAVESITE</li>
    <li class="service-item" style="top:578px">PAYMENT ENSURED<br>FOREVER GRAVE CAR</li>
    <li class="service-item" style="top:614px">PAYMENT ENSURED<br>FOREVER GRAVE CAR</li>
    <li class="service-item" style="top:649px">WEDDING &amp; TRIMMING ON<br>YOUR GRAVESITE</li>
    <li class="service-item" style="top:685px">PAYMENT ENSURED<br>FOREVER GRAVE CAR</li>
  </ul>
  <p class="valid">Valid through<br>10/31/22</p>

  <!-- Seasonal -->
  <section class="plan plan-side seasonal">
    <div class="plan-head"><span class="plan-name">SEASONAL</span><span class="plan-sub">CARE ENDOWMENT</span></div>
    <div class="plan-body">
      <p class="plan-freq" style="top:12px">Approximately every 7 weeks<br>during the growing season:<br>Mid-April through Mid-October</p>
      <svg class="mark" style="top:54px" viewBox="0 0 16 16"><circle cx="8" cy="8" r="7" fill="none" stroke="#fff" stroke-width="1.3"/><path d="M5.3 5.3l5.4 5.4M10.7 5.3l-5.4 5.4" stroke="#fff" stroke-width="1.3"/></svg>
      <svg class="mark" style="top:92px" viewBox="0 0 16 16"><circle cx="8" cy="8" r="7" fill="none" stroke="#fff" stroke-width="1.3"/><path d="M5.3 5.3l5.4 5.4M10.7 5.3l-5.4 5.4" stroke="#fff" stroke-width="1.3"/></svg>
      <svg class="mark" style="top:128px" viewBox="0 0 16 16"><circle cx="8" cy="8" r="7" fill="none" stroke="#fff" stroke-width="1.3"/><path d="M5.3 5.3l5.4 5.4M10.7 5.3l-5.4 5.4" stroke="#fff" stroke-width="1.3"/></svg>
      <svg class="mark" style="top:164px" viewBox="0 0 16 16"><circle cx="8" cy="8" r="7" fill="none" stroke="#fff" stroke-width="1.3"/><path d="M5.3 5.3l5.4 5.4M10.7 5.3l-5.4 5.4" stroke="#fff" stroke-width="1.3"/></svg>
      <svg class="mark" style="top:200px" viewBox="0 0 16 16"><circle cx="8" cy="8" r="7" fill="none" stroke="#fff" stroke-width="1.3"/><path d="M5.3 5.3l5.4 5.4M10.7 5.3l-5.4 5.4" stroke="#fff" stroke-width="1.3"/></svg>
      <svg class="mark" style="top:235px" viewBox="0 0 16 16"><circle cx="8" cy="8" r="7" fill="none" stroke="#fff" stroke-width="1.3"/><path d="M5.3 5.3l5.4 5.4M10.7 5.3l-5.4 5.4" stroke="#fff" stroke-width="1.3"/></svg>
      <div class="rule" style="top:260px;left:12px;right:12px"></div>
      <div class="price-row" style="top:268px">
        <span class="price"><b>$357</b><small>3 Years</small></span>
        <span class="price"><b>$238</b><small>2 Years</small></span>
        <span class="price"><b>$119</b><small>1 Years</small></span>
      </div>
      <p class="note" style="top:301px">Multi-year payment locks<br>in current rates.</p>
    </div>
  </section>

  <!-- Perpetual -->
  <div class="badge" aria-hidden="false"><span>Most</span><span>Popular</span></div>
  <section class="plan perpetual">
    <div class="plan-head"><span class="plan-name">PERPETUAL</span><span class="plan-sub">CARE ENDOWMENT</span></div>
    <p class="plan-freq" style="top:76px">Approximately every 7 weeks<br>during the growing season:<br>Mid-April through Mid-October</p>
    <svg class="mark" style="top:131px" viewBox="0 0 16 16"><circle cx="8" cy="8" r="7" fill="none" stroke="var(--maroon)" stroke-width="1.3"/><path d="M4.8 8.3l2.2 2.2 4.2-4.8" fill="none" stroke="var(--maroon)" stroke-width="1.4"/></svg>
    <svg class="mark" style="top:171px" viewBox="0 0 16 16"><circle cx="8" cy="8" r="7" fill="none" stroke="var(--maroon)" stroke-width="1.3"/><path d="M4.8 8.3l2.2 2.2 4.2-4.8" fill="none" stroke="var(--maroon)" stroke-width="1.4"/></svg>
    <svg class="mark" style="top:209px" viewBox="0 0 16 16"><circle cx="8" cy="8" r="7" fill="none" stroke="var(--maroon)" stroke-width="1.3"/><path d="M4.8 8.3l2.2 2.2 4.2-4.8" fill="none" stroke="var(--maroon)" stroke-width="1.4"/></svg>
    <svg class="mark" style="top:248px" viewBox="0 0 16 16"><circle cx="8" cy="8" r="7" fill="none" stroke="var(--maroon)" stroke-width="1.3"/><path d="M4.8 8.3l2.2 2.2 4.2-4.8" fill="none" stroke="var(--maroon)" stroke-width="1.4"/></svg>
    <svg class="mark" style="top:286px" viewBox="0 0 16 16"><circle cx="8" cy="8" r="7" fill="none" stroke="var(--maroon)" stroke-width="1.3"/><path d="M4.8 8.3l2.2 2.2 4.2-4.8" fill="none" stroke="var(--maroon)" stroke-width="1.4"/></svg>
    <svg class="mark" style="top:324px" viewBox="0 0 16 16"><circle cx="8" cy="8" r="7" fill="none" stroke="var(--maroon)" stroke-width="1.3"/><path d="M4.8 8.3l2.2 2.2 4.2-4.8" fill="none" stroke="var(--maroon)" stroke-width="1.4"/></svg>
    <div class="rule" style="top:340px;left:24px;right:24px"></div>
    <p class="price-big" style="top:350px;font-size:22px;color:var(--maroon)">$313</p>
    <p class="note" style="top:377px;color:var(--maroon)">12 Monthly payments.<br>Call for single payment<br>discount.</p>
  </section>

  <!-- Basic -->
  <section class="plan plan-side basic">
    <div class="plan-head"><span class="plan-name">BASIC</span><span class="plan-sub">CARE ENDOWMENT</span></div>
    <div class="plan-body">
      <p class="plan-freq" style="top:12px">2 times per year:<br>Mid-May &amp; Mid-September</p>
      <svg class="mark" style="top:54px" viewBox="0 0 16 16"><circle cx="8" cy="8" r="7" fill="none" stroke="#fff" stroke-width="1.3"/><path d="M4.8 8.3l2.2 2.2 4.2-4.8" fill="none" stroke="#fff" stroke-width="1.4"/></svg>
      <svg class="mark" style="top:92px" viewBox="0 0 16 16"><circle cx="8" cy="8" r="7" fill="none" stroke="#fff" stroke-width="1.3"/><path d="M4.8 8.3l2.2 2.2 4.2-4.8" fill="none" stroke="#fff" stroke-width="1.4"/></svg>
      <svg class="mark" style="top:128px" viewBox="0 0 16 16"><circle cx="8" cy="8" r="7" fill="none" stroke="#fff" stroke-width="1.3"/><path d="M5.3 5.3l5.4 5.4M10.7 5.3l-5.4 5.4" stroke="#fff" stroke-width="1.3"/></svg>
      <svg class="mark" style="top:164px" viewBox="0 0 16 16"><circle cx="8" cy="8" r="7" fill="none" stroke="#fff" stroke-width="1.3"/><path d="M5.3 5.3l5.4 5.4M10.7 5.3l-5.4 5.4" stroke="#fff" stroke-width="1.3"/></svg>
      <svg class="mark" style="top:200px" viewBox="0 0 16 16"><circle cx="8" cy="8" r="7" fill="none" stroke="#fff" stroke-width="1.3"/><path d="M5.3 5.3l5.4 5.4M10.7 5.3l-5.4 5.4" stroke="#fff" stroke-width="1.3"/></svg>
      <svg class="mark" style="top:235px" viewBox="0 0 16 16"><circle cx="8" cy="8" r="7" fill="none" stroke="#fff" stroke-width="1.3"/><path d="M5.3 5.3l5.4 5.4M10.7 5.3l-5.4 5.4" stroke="#fff" stroke-width="1.3"/></svg>
      <div class="rule" style="top:260px;left:12px;right:12px"></div>
      <p class="price-big" style="top:268px;font-size:20px">$255</p>
      <p class="note" style="top:292px">12 Monthly payments.<br>Call for single payment<br>discount.</p>
    </div>
  </section>

  <footer>
    <div class="footer-band">48 Willow Lane, Fairhaven NJ 07000</div>
    <p class="footer-contact">(555) 014-2290 &nbsp;|&nbsp; elmwoodgrove.org</p>
    <div class="footer-rule"></div>
  </footer>
</main>
</body>
</html>
```